Velmora.net - A website for sensual content creators (like PeakPatron)

Web Design Contest for Velmora.net
Overview: Velmora.net is set to be the next big name in the world of content creation, blending a modern social media platform with exclusive 18+ paid content. Unlike competitors like PeakPatron and Subvio, Velmora.net will offer a unique and intuitive user experience that stands out for its clean, modern design and effortless usability.

Platform Features:

Dual Content Modes: Velmora.net offers a mix of safe-for-work social media content, alongside private and paid media for 18+ users.
Content Creators Hub: A space for creators to share sensual, engaging, and private media, with opportunities to grow their fanbase and monetize their work.
Live Streaming & Messaging: Creators can connect with their audience through live streams and private messages (both live and asynchronous).
Community Building: Users can explore content, interact with creators, and engage in a rich social experience.
Design Goals:

Front Page (Logged Out): The landing page should captivate new visitors while clearly outlining what Velmora.net offers. A balance of intrigue and professionalism is key here. The goal is to attract both content creators and consumers, showcasing the platform's potential in an elegant and tasteful manner. Minimalistic yet bold, the design should avoid overwhelming visitors with too much information but leave a lasting impression. The color palette, fonts, and imagery should feel fresh, clean, and inviting.

Logged-In Dashboard: This design should prioritize easy navigation for creators and users alike. Think of a sleek, customizable dashboard where everything is at your fingertips—from content creation tools to messaging, analytics, and payment settings. The user experience should feel smooth and modern without sacrificing functionality. Visual clarity and an emphasis on user empowerment are crucial.

Messaging Page (Live Chat): The live chat feature needs to feel dynamic and interactive, with a design that makes real-time conversations feel personal and engaging. Consider features like reactions, media sharing, and notifications—all wrapped up in a sleek interface. The layout should encourage interaction while remaining clean and distraction-free.

Normal Chat: For asynchronous messaging, aim for a layout that balances simplicity and depth. Users should be able to easily track their conversations, search through chats, and engage in a natural flow. Think of it as a hybrid between social messaging apps and content creator tools, offering the best of both worlds in a clutter-free space.

Style & Aesthetic: We’re looking for a design that’s modern, sleek, and minimal but still leaves room for personality. It should feel fresh and distinct from the competition. Focus on UX/UI that feels unique to Velmora.net, ensuring that navigation is effortless and the platform is approachable to both creators and consumers. Avoid the heavy, cluttered feel of other platforms—this needs to be light, easy to use, and beautifully crafted. Clean lines, innovative layout, and a user-first experience are key here.

Target Market(s)

Women

Industry/Entity Type

Adult/Content Creation

Number of Pages Required

5+ page

Colors

Designer to choose only greyscale colors for use in the design.

Requirements
Must have
• Front page, logged in page (with feed/etc), streaming page (1-1), and chat page.
Nice to have
• I just want something unique that stands out. I do not want a 1:1 copy of PeakPatron or Subvoi. The feel of the site should be classy but mordern and sensual. We want to attract people and avoid looking like a porn site (which we're not)

```html
<!DOCTYPE html>
<html lang="en">
<head>
<meta charset="utf-8">
<title>Velmora.net — Screens</title>
<link href="https://fonts.googleapis.com/css2?family=Montserrat:wght@400;500;600;700&family=Lato:wght@400;700&display=swap" rel="stylesheet">
<style>
:root{
  --bg:#7f7f7f;
  --white:#ffffff;
  --ink:#111111;
  --field:#d9d9d9;
  --mute:#7a7a7a;
  --head:"Montserrat",sans-serif;
  --body:"Lato",sans-serif;
}
*{box-sizing:border-box;margin:0;padding:0}
html,body{width:1200px;height:788px;overflow:hidden;background:var(--bg)}
.board{position:absolute;left:0;top:0;width:2380px;height:1564px;transform:scale(.50420);transform-origin:0 0;font-family:var(--body);color:var(--ink)}
.screen{position:absolute;width:583px;height:378px;background:var(--white);overflow:hidden}
.abs{position:absolute}

/* photo areas: soft tonal fields */
.photo{position:absolute}
.photo.portrait{background:
  radial-gradient(ellipse 130px 150px at 32% 38%,#e8e8e8 0%,#bcbcbc 45%,transparent 75%),
  radial-gradient(ellipse 110px 120px at 50% 75%,#f2f2f2 0%,#cfcfcf 50%,transparent 80%),
  radial-gradient(ellipse 90px 110px at 15% 20%,#2a2a2a 0%,transparent 80%),
  linear-gradient(115deg,#1c1c1c 0%,#5a5a5a 35%,#8d8d8d 60%,#3e3e3e 100%)}
.photo.portrait.faded{background:
  radial-gradient(ellipse 130px 150px at 32% 38%,#f4f4f4 0%,#dedede 45%,transparent 75%),
  radial-gradient(ellipse 110px 120px at 52% 72%,#fafafa 0%,#e4e4e4 50%,transparent 80%),
  linear-gradient(115deg,#8a8a8a 0%,#b8b8b8 35%,#d6d6d6 60%,#c2c2c2 100%)}
.photo.stream{background:
  radial-gradient(ellipse 120px 190px at 38% 35%,#f5f5f5 0%,#c9c9c9 40%,transparent 75%),
  radial-gradient(ellipse 80px 130px at 30% 85%,#e0e0e0 0%,transparent 80%),
  radial-gradient(ellipse 50px 70px at 90% 80%,#f0f0f0 0%,transparent 80%),
  linear-gradient(95deg,#2b2b2b 0%,#6c6c6c 30%,#a8a8a8 55%,#8a8a8a 80%,#b4b4b4 100%)}
.thumb{background:
  radial-gradient(ellipse 45px 55px at 38% 45%,#121212 0%,#3a3a3a 50%,transparent 85%),
  radial-gradient(ellipse 40px 40px at 85% 25%,#e6e6e6 0%,transparent 85%),
  linear-gradient(100deg,#6a6a6a,#b5b5b5 55%,#dcdcdc)}
.thumb.hi{background:
  radial-gradient(ellipse 38px 45px at 45% 40%,#dadada 0%,#8d8d8d 45%,transparent 80%),
  radial-gradient(ellipse 70px 70px at 35% 55%,#0e0e0e 0%,#2e2e2e 60%,transparent 90%),
  linear-gradient(100deg,#1a1a1a,#6a6a6a 55%,#cfcfcf)}

/* brand */
.brand{position:absolute;font-family:var(--head);font-weight:500;color:var(--ink);letter-spacing:-.3px;white-space:nowrap}
.brand.sm{font-size:16px}
.brand.lg{font-size:28px}

/* header */
.topbar{position:absolute;left:0;top:0;width:100%;height:45px;background:var(--white);box-shadow:0 2px 6px rgba(0,0,0,.12);z-index:2}
.topbar .brand{left:23px;top:12px}
.mode-toggle{position:absolute;width:52px;height:24px;border-radius:12px;background:#e4e4e4}
.mode-toggle .eye{position:absolute;left:6px;top:7px}
.mode-toggle .knob{position:absolute;right:0;top:0;width:24px;height:24px;border-radius:50%;background:var(--ink)}
.mode-toggle .knob svg{position:absolute;left:5px;top:7px}
.avatar-btn{position:absolute;width:24px;height:24px;border-radius:50%;border:1px solid #ddd;background:#f3f3f3}
.avatar-btn svg{position:absolute;left:5px;top:4px}
.pill-btn{position:absolute;background:var(--ink);color:var(--white);border-radius:13px;font:500 11px var(--head);display:flex;align-items:center;justify-content:center}

/* sections */
.sec-title{position:absolute;font:600 17px var(--head);display:flex;align-items:baseline;gap:16px;white-space:nowrap}
.sec-title small{font:600 8.5px var(--head)}

/* cards */
.card{position:absolute;width:165px;height:137px;background:var(--white);border-radius:8px;box-shadow:0 1px 5px rgba(0,0,0,.18);overflow:hidden}
.card .thumb{position:absolute;left:0;top:0;width:100%;height:97px}
.card .dur{position:absolute;right:6px;bottom:5px;font:700 8.5px var(--body);color:var(--ink);background:rgba(255,255,255,.75);padding:0 3px;border-radius:2px}
.card .live{position:absolute;left:9px;top:10px;height:15px;padding:0 7px 0 15px;border-radius:3px;background:var(--white);border:1px solid var(--ink);font:700 8.5px/13px var(--body)}
.card .live::before{content:"";position:absolute;left:5px;top:4.5px;width:5px;height:5px;border-radius:50%;background:var(--ink)}
.card .title{position:absolute;left:12px;top:104px;font:700 11px var(--body)}
.card .creator{position:absolute;left:12px;top:120px;font:400 8.5px var(--body);color:var(--mute)}
.pointer{position:absolute}

/* login */
.login-card{position:absolute;background:var(--white)}
.login-card .heading{position:absolute;width:100%;text-align:center;font:500 17px var(--head)}
.field{position:absolute;width:178px;height:36px;border-radius:18px;background:var(--field);font:400 9.5px var(--body);color:#555;padding-left:14px;display:flex;align-items:center}
.link{position:absolute;font:400 8.5px var(--body);white-space:nowrap}

/* hero */
.hero{position:absolute;left:0;top:46px;width:100%;height:124px;background:
  radial-gradient(ellipse 120px 90px at 30% 60%,#f3f3f3 0%,transparent 80%),
  linear-gradient(90deg,#bdbdbd,#e6e6e6 35%,#dadada 70%,#a9a9a9)}
.hero h1{position:absolute;width:100%;top:13px;text-align:center;font:400 18px var(--head);letter-spacing:.4px}
.hero p{position:absolute;left:146px;width:290px;top:45px;text-align:center;font:400 8.5px/10px var(--body)}

/* dashboard tiles */
.tile{position:absolute;width:85px;height:84px;background:var(--white);border-radius:8px;box-shadow:0 1px 5px rgba(0,0,0,.16);text-align:center}
.tile svg{position:absolute;left:27px;top:16px}
.tile span{position:absolute;left:0;width:100%;top:55px;font:400 9px var(--body)}

/* chat */
.chat-title{position:absolute;font:600 17px var(--head);display:flex;align-items:center;gap:9px}
.comment{position:absolute;font:400 8.5px var(--body);display:flex;align-items:center;gap:5px;white-space:nowrap}
.comment i{display:inline-block;width:11px;height:11px;border-radius:2px;background:#9a9a9a}
.comment i.pale{background:#d6d6d6}
.comment em{font-style:normal;color:#9a9a9a}
.comment em.pale{color:#c8c8c8}
.notice{position:absolute;left:0;width:100%;height:24px;background:#e6e6e6;font:400 8px var(--body);color:#888;padding-left:14px;display:flex;align-items:center}
.msg-input{position:absolute;height:23px;border-radius:12px;background:#e4e4e4;font:400 8px var(--body);color:#999;padding-left:10px;display:flex;align-items:center}
.msg-input svg{position:absolute;right:6px;top:6px}
.live-tag{position:absolute;height:14px;width:40px;border-radius:3px;background:var(--white);font:400 8px/14px var(--body);color:#888;padding-left:14px}
.live-tag::before{content:"";position:absolute;left:5px;top:4.5px;width:5px;height:5px;border-radius:50%;background:#888}
.thread{position:absolute;left:6px;width:158px;height:31px;border-bottom:1px solid #e2e2e2}
.thread svg{position:absolute;left:6px;top:6px}
.thread b{position:absolute;left:34px;top:4px;font:700 10.5px var(--body)}
.thread span{position:absolute;left:34px;top:17px;font:400 7.5px var(--body);color:#444}
.bubble{position:absolute;height:24px;border-radius:12px;font:400 7.5px var(--body);display:flex;align-items:center;justify-content:center;white-space:nowrap}
.stamp{position:absolute;font:400 6.5px var(--body);color:#999}
</style>
</head>
<body>
<svg width="0" height="0" style="position:absolute">
  <defs>
    <symbol id="eye" viewBox="0 0 14 10"><path d="M1 5C3 1.5 11 1.5 13 5C11 8.5 3 8.5 1 5Z" fill="none" stroke="#777" stroke-width="1"/><circle cx="7" cy="5" r="1.6" fill="#777"/></symbol>
    <symbol id="oval" viewBox="0 0 14 10"><ellipse cx="7" cy="5" rx="6" ry="3.5" fill="none" stroke="#fff" stroke-width="1.2"/><path d="M1 5H13" stroke="#fff" stroke-width=".8"/></symbol>
    <symbol id="person" viewBox="0 0 14 16"><circle cx="7" cy="5" r="3.2" fill="#bbb"/><path d="M1 15C1 10 13 10 13 15Z" fill="#bbb"/></symbol>
    <symbol id="person-dark" viewBox="0 0 20 20"><circle cx="10" cy="10" r="9" fill="none" stroke="#111" stroke-width="1.4"/><circle cx="10" cy="8" r="3.2" fill="#111"/><path d="M4.5 16C5.5 11.5 14.5 11.5 15.5 16Z" fill="#111"/></symbol>
    <symbol id="arrow" viewBox="0 0 20 20"><path d="M2 2L18 9L11 11L8 18Z" fill="#111"/></symbol>
    <symbol id="smile" viewBox="0 0 12 12"><circle cx="6" cy="6" r="5" fill="none" stroke="#aaa" stroke-width=".9"/><path d="M3.5 7C4.5 8.6 7.5 8.6 8.5 7" fill="none" stroke="#aaa" stroke-width=".9"/></symbol>
    <symbol id="gift" viewBox="0 0 32 32"><rect x="3" y="10" width="26" height="6" fill="currentColor"/><rect x="5" y="17" width="22" height="13" fill="currentColor"/><rect x="14.5" y="10" width="3" height="20" fill="#fff" opacity=".6"/><path d="M16 10C12 2 6 4 9 9M16 10C20 2 26 4 23 9" fill="none" stroke="currentColor" stroke-width="2"/></symbol>
  </defs>
</svg>

<main class="board">

  <!-- Login, photo backdrop -->
  <section class="screen" style="left:14px;top:14px">
    <div class="photo portrait" style="left:0;top:0;width:583px;height:378px" role="img" aria-label="Black and white photo of a smiling young man holding a puppy"></div>
    <div class="login-card" style="left:345px;top:13px;width:224px;height:351px;border-radius:16px">
      <div class="brand lg" style="left:0;width:100%;text-align:center;top:48px">Velmora</div>
      <div class="heading" style="top:107px">Login</div>
      <div class="field" style="left:22px;top:148px">Username/Email</div>
      <div class="field" style="left:22px;top:197px">Password</div>
      <div class="link" style="left:22px;top:245px">Create an Account</div>
      <div class="link" style="right:23px;top:245px">Forgot Password</div>
      <div class="pill-btn" style="left:71px;top:287px;width:74px;height:24px">Login</div>
    </div>
  </section>

  <!-- Explore feed -->
  <section class="screen" style="left:604px;top:14px">
    <header class="topbar">
      <div class="brand sm">Velmora</div>
      <div class="mode-toggle" style="left:476px;top:10px"><svg class="eye" width="12" height="10"><use href="#eye"/></svg><div class="knob"><svg width="14" height="10"><use href="#oval"/></svg></div></div>
      <div class="avatar-btn" style="left:544px;top:10px"><svg width="14" height="16"><use href="#person"/></svg></div>
    </header>
    <div class="sec-title" style="left:19px;top:62px">Explore <small>See more</small></div>
    <div class="card" style="left:18px;top:95px"><div class="thumb" role="img" aria-label="Video thumbnail of a creator"><span class="dur">30:00</span></div><div class="title">Video Title</div><div class="creator">Creator</div></div>
    <div class="card" style="left:209px;top:95px"><div class="thumb hi" role="img" aria-label="Video thumbnail of a creator"><span class="dur">30:00</span></div><div class="title">Video Title</div><div class="creator">Creator</div></div>
    <div class="card" style="left:399px;top:95px"><div class="thumb" role="img" aria-label="Video thumbnail of a creator"><span class="dur">30:00</span></div><div class="title">Video Title</div><div class="creator">Creator</div></div>
    <svg class="pointer" style="left:362px;top:203px" width="22" height="22"><use href="#arrow"/></svg>
    <div class="sec-title" style="left:19px;top:251px">Followed <small>See more</small></div>
    <div class="card" style="left:18px;top:284px"><div class="thumb" role="img" aria-label="Live stream thumbnail"><span class="live">Live</span><span class="dur">30:00</span></div></div>
    <div class="card" style="left:209px;top:284px"><div class="thumb" role="img" aria-label="Live stream thumbnail"><span class="live">Live</span><span class="dur">30:00</span></div></div>
    <div class="card" style="left:399px;top:284px"><div class="thumb" role="img" aria-label="Live stream thumbnail"><span class="live">Live</span><span class="dur">30:00</span></div></div>
  </section>

  <!-- Live stream with comments -->
  <section class="screen" style="left:1193px;top:14px;background:transparent">
    <div class="photo stream" style="left:173px;top:0;width:410px;height:378px" role="img" aria-label="Live stream video of a blonde creator"></div>
    <svg class="abs" style="left:380px;top:8px" width="90" height="45"><path d="M5 42L42 10L82 42" fill="none" stroke="#222" stroke-width="2"/></svg>
    <svg class="abs" style="left:380px;top:320px" width="84" height="60"><circle cx="42" cy="42" r="38" fill="none" stroke="#222" stroke-width="2"/><path d="M34 26L56 42L34 58Z" fill="none" stroke="#222" stroke-width="2"/></svg>
    <div class="live-tag" style="left:520px;top:14px">Live</div>
    <aside class="abs" style="left:0;top:0;width:173px;height:378px;background:var(--white);border-radius:14px 0 0 14px">
      <div class="chat-title" style="left:12px;top:12px"><svg width="10" height="14"><path d="M8 1L2 7L8 13" fill="none" stroke="#111" stroke-width="1.8"/></svg>Chats</div>
      <div class="comment" style="left:14px;top:52px"><i></i><em>User:</em>User Commented Here</div>
      <div class="comment" style="left:14px;top:76px"><i class="pale"></i><em class="pale">User:</em>User Commented Here</div>
      <div class="comment" style="left:14px;top:100px"><i></i><em>User:</em>User Commented Here</div>
      <div class="comment" style="left:14px;top:122px"><em class="pale">User:</em>User Commented Here</div>
      <div class="comment" style="left:14px;top:142px"><em>User:</em>User Commented Here</div>
      <div class="notice" style="top:165px">User just subscribed to your package</div>
      <div class="comment" style="left:14px;top:202px"><i class="pale"></i><em class="pale">User:</em>User Commented Here</div>
      <div class="comment" style="left:14px;top:225px"><em>User:</em>User Commented Here</div>
      <div class="comment" style="left:14px;top:245px"><em class="pale">User:</em>User Commented Here</div>
      <div class="comment" style="left:14px;top:266px"><em>User:</em>User Commented Here</div>
      <div class="comment" style="left:14px;top:287px"><i></i><em>User:</em>User Commented Here</div>
      <div class="comment" style="left:14px;top:310px"><em class="pale">User:</em>User Commented Here</div>
      <div class="msg-input" style="left:8px;top:346px;width:134px">Send a message<svg width="11" height="11"><use href="#smile"/></svg></div>
      <svg class="abs" style="left:154px;top:350px" width="6" height="16"><circle cx="3" cy="2" r="1.7" fill="#111"/><circle cx="3" cy="8" r="1.7" fill="#111"/><circle cx="3" cy="14" r="1.7" fill="#111"/></svg>
    </aside>
  </section>

  <!-- Direct messages -->
  <section class="screen" style="left:1783px;top:14px;background:transparent">
    <aside class="abs" style="left:0;top:0;width:172px;height:378px;background:var(--white);border-radius:14px 0 0 14px">
      <div class="chat-title" style="left:12px;top:12px"><svg width="10" height="14"><path d="M8 1L2 7L8 13" fill="none" stroke="#111" stroke-width="1.8"/></svg>Chats</div>
      <svg class="abs" style="left:147px;top:18px" width="16" height="12"><rect x="1" y="1" width="14" height="10" fill="none" stroke="#111" stroke-width="1.3"/><path d="M1 1L8 7L15 1" fill="none" stroke="#111" stroke-width="1.3"/></svg>
      <div class="thread" style="top:48px"><svg width="20" height="20"><use href="#person-dark"/></svg><b>User</b><span>Last Message</span></div>
      <div class="thread" style="top:79px"><svg width="20" height="20"><use href="#person-dark"/></svg><b>User</b><span>Last Message</span></div>
      <div class="thread" style="top:111px"><svg width="20" height="20"><use href="#person-dark"/></svg><b>User</b><span>Last Message</span></div>
      <div class="thread" style="top:142px"><svg width="20" height="20"><use href="#person-dark"/></svg><b>User</b><span>Last Message</span></div>
      <div class="thread" style="top:174px"><svg width="20" height="20"><use href="#person-dark"/></svg><b>User</b><span>Last Message</span></div>
      <div class="thread" style="top:205px"><svg width="20" height="20"><use href="#person-dark"/></svg><b>User</b><span>Last Message</span></div>
      <div class="thread" style="top:237px"><svg width="20" height="20"><use href="#person-dark"/></svg><b>User</b><span>Last Message</span></div>
      <div class="thread" style="top:268px"><svg width="20" height="20"><use href="#person-dark"/></svg><b>User</b><span>Last Message</span></div>
      <div class="thread" style="top:300px"><svg width="20" height="20"><use href="#person-dark"/></svg><b>User</b><span>Last Message</span></div>
      <div class="thread" style="top:331px;border-bottom:0"><svg width="20" height="20"><use href="#person-dark"/></svg><b>User</b><span>Last Message</span></div>
    </aside>
    <div class="abs" style="left:174px;top:0;width:409px;height:378px;background:var(--white)">
      <div class="abs" style="left:0;top:0;width:100%;height:43px;background:#8c8c8c"></div>
      <svg class="abs" style="left:12px;top:12px" width="20" height="20"><use href="#person-dark"/></svg>
      <div class="abs" style="left:38px;top:10px;font:700 10.5px var(--body)">User</div>
      <div class="abs" style="left:38px;top:24px;font:400 7px var(--body)">Active Now</div>
      <svg class="abs" style="left:390px;top:14px" width="6" height="16"><circle cx="3" cy="2" r="1.6" fill="#111"/><circle cx="3" cy="8" r="1.6" fill="#111"/><circle cx="3" cy="14" r="1.6" fill="#111"/></svg>
      <svg class="abs" style="left:22px;top:260px" width="18" height="18"><use href="#person-dark"/></svg>
      <div class="bubble" style="left:43px;top:252px;width:100px;background:#dedede">User sent you a message.</div>
      <div class="stamp" style="left:44px;top:280px">3:30 PM</div>
      <div class="bubble" style="left:270px;top:296px;width:102px;background:var(--ink);color:var(--white)">You sent you a message.</div>
      <svg class="abs" style="left:377px;top:302px" width="20" height="20"><use href="#person-dark"/></svg>
      <div class="stamp" style="left:350px;top:325px">3:30 PM</div>
      <div class="msg-input" style="left:18px;top:346px;width:378px;height:22px">Send a message<svg width="11" height="11"><use href="#smile"/></svg></div>
    </div>
  </section>

  <!-- Login with welcome copy -->
  <section class="screen" style="left:14px;top:400px">
    <div class="photo portrait faded" style="left:0;top:0;width:583px;height:378px" role="img" aria-label="Faded black and white photo of a smiling young man holding a puppy"></div>
    <div class="abs" style="left:23px;top:264px;font:400 17px var(--head);letter-spacing:.4px">Welcome to Velmora.net</div>
    <p class="abs" style="left:23px;top:294px;width:262px;font:400 8.5px/10.5px var(--body)">Where Passion Meets Creativity At Velmora.net, we believe in the power of expression. Whether you're a content creator or a fan, our platform is designed to bring out the best in creativity, connection, and community. Share intimate moments, unlock exclusive content, and discover a new way to connect with your favorite creators like never before.</p>
    <div class="login-card" style="left:344px;top:0;width:239px;height:378px;border-radius:16px 0 0 16px">
      <div class="brand lg" style="left:0;width:100%;text-align:center;top:62px">Velmora</div>
      <div class="heading" style="top:120px">Login</div>
      <div class="field" style="left:34px;top:160px">Username/Email</div>
      <div class="field" style="left:34px;top:209px">Password</div>
      <div class="link" style="left:34px;top:257px">Create an Account</div>
      <div class="link" style="right:27px;top:257px">Forgot Password</div>
      <div class="pill-btn" style="left:82px;top:299px;width:74px;height:24px">Login</div>
    </div>
  </section>

  <!-- Feed with search -->
  <section class="screen" style="left:604px;top:400px">
    <header class="topbar">
      <div class="brand sm">Velmora</div>
      <div class="mode-toggle" style="left:476px;top:10px"><svg class="eye" width="12" height="10"><use href="#eye"/></svg><div class="knob"><svg width="14" height="10"><use href="#oval"/></svg></div></div>
      <div class="avatar-btn" style="left:544px;top:10px"><svg width="14" height="16"><use href="#person"/></svg></div>
    </header>
    <div class="abs" style="left:19px;top:70px;width:544px;height:28px;border-radius:14px;border:1px solid #ddd;box-shadow:0 1px 4px rgba(0,0,0,.1);font:400 9px/26px var(--body);color:#aaa;padding-left:29px">Search
      <svg class="abs" style="left:13px;top:9px" width="9" height="9"><circle cx="3.7" cy="3.7" r="2.8" fill="none" stroke="#aaa" stroke-width="1"/><path d="M5.8 5.8L8.5 8.5" stroke="#aaa" stroke-width="1"/></svg>
    </div>
    <div class="sec-title" style="left:19px;top:124px">Explore <small>See more</small></div>
    <div class="card" style="left:18px;top:157px"><div class="thumb" role="img" aria-label="Video thumbnail of a creator"><span class="dur">30:00</span></div><div class="title">Video Title</div><div class="creator">Creator</div></div>
    <div class="card" style="left:209px;top:157px"><div class="thumb hi" role="img" aria-label="Video thumbnail of a creator"><span class="dur">30:00</span></div><div class="title">Video Title</div><div class="creator">Creator</div></div>
    <div class="card" style="left:399px;top:157px"><div class="thumb" role="img" aria-label="Video thumbnail of a creator"><span class="dur">30:00</span></div><div class="title">Video Title</div><div class="creator">Creator</div></div>
    <svg class="pointer" style="left:362px;top:265px" width="22" height="22"><use href="#arrow"/></svg>
    <div class="sec-title" style="left:19px;top:313px">Followed <small>See more</small></div>
    <div class="card" style="left:18px;top:346px"><div class="thumb" role="img" aria-label="Live stream thumbnail"><span class="live">Live</span></div></div>
    <div class="card" style="left:209px;top:346px"><div class="thumb" role="img" aria-label="Live stream thumbnail"><span class="live">Live</span></div></div>
    <div class="card" style="left:399px;top:346px"><div class="thumb" role="img" aria-label="Live stream thumbnail"><span class="live">Live</span></div></div>
  </section>

  <!-- Creator live view -->
  <section class="screen" style="left:1193px;top:400px">
    <div class="photo stream" style="left:0;top:0;width:583px;height:378px" role="img" aria-label="Creator's own live stream video"></div>
    <div class="abs" style="left:0;top:0;width:210px;height:378px;background:linear-gradient(90deg,rgba(0,0,0,.55),rgba(0,0,0,0))"></div>
    <div class="pill-btn" style="left:14px;top:10px;width:90px;height:25px;background:var(--white);color:var(--ink);font-size:11px">End Live</div>
    <div class="live-tag" style="left:520px;top:14px">Live</div>
    <svg class="abs" style="left:78px;top:76px;color:#d8d8d8" width="48" height="48"><use href="#gift"/></svg>
    <div class="abs" style="left:16px;top:132px;width:170px;text-align:center;font:500 15px/19px var(--head);color:var(--white)">Notification Alerts Here</div>
    <div class="abs" style="left:14px;top:230px;width:181px;height:133px;background:var(--white);border-radius:12px">
      <div class="chat-title" style="left:12px;top:12px"><svg width="10" height="14"><path d="M8 1L2 7L8 13" fill="none" stroke="#111" stroke-width="1.8"/></svg>Chats</div>
      <div class="comment" style="left:14px;top:47px"><i class="pale"></i><em class="pale">User:</em>User Commented Here</div>
      <div class="comment" style="left:14px;top:71px"><i></i><em>User:</em>User Commented Here</div>
      <div class="comment" style="left:14px;top:94px"><em>User:</em>User Commented Here</div>
    </div>
  </section>

  <!-- Landing, logged out (two states) -->
  <section class="screen" style="left:14px;top:786px">
    <header class="topbar">
      <div class="brand sm" style="top:12px">Velmora</div>
      <div class="mode-toggle" style="left:98px;top:8px"><svg class="eye" width="12" height="10"><use href="#eye"/></svg><div class="knob"><svg width="14" height="10"><use href="#oval"/></svg></div></div>
      <div class="pill-btn" style="left:494px;top:9px;width:75px;height:25px">Login</div>
    </header>
    <div class="hero" role="img" aria-label="Faded banner photo of a young man with a puppy"><h1>Welcome to Velmora.net</h1><p>Where Passion Meets Creativity At Velmora.net, we believe in the power of expression. Whether you're a content creator or a fan, our platform is designed to bring out the best in creativity, connection, and community. Share intimate moments, unlock exclusive content, and discover a new way to connect with your favorite creators like never before.</p></div>
    <div class="sec-title" style="left:19px;top:183px">Explore</div>
    <div class="card" style="left:19px;top:217px"><div class="thumb" role="img" aria-label="Video thumbnail of a creator"><span class="dur">30:00</span></div><div class="title">Video Title</div><div class="creator">Creator</div></div>
    <div class="card" style="left:209px;top:217px"><div class="thumb hi" role="img" aria-label="Video thumbnail of a creator"><span class="dur">30:00</span></div><div class="title">Video Title</div><div class="creator">Creator</div></div>
    <div class="card" style="left:399px;top:217px"><div class="thumb" role="img" aria-label="Video thumbnail of a creator"><span class="dur">30:00</span></div><div class="title">Video Title</div><div class="creator">Creator</div></div>
    <svg class="pointer" style="left:362px;top:325px" width="22" height="22"><use href="#arrow"/></svg>
  </section>

  <section class="screen" style="left:14px;top:1172px">
    <header class="topbar">
      <div class="brand sm" style="top:12px">Velmora</div>
      <div class="mode-toggle" style="left:98px;top:8px"><svg class="eye" width="12" height="10"><use href="#eye"/></svg><div class="knob"><svg width="14" height="10"><use href="#oval"/></svg></div></div>
      <div class="pill-btn" style="left:494px;top:9px;width:75px;height:25px">Login</div>
    </header>
    <div class="hero" role="img" aria-label="Faded banner photo of a young man with a puppy"><h1>Welcome to Velmora.net</h1><p>Where Passion Meets Creativity At Velmora.net, we believe in the power of expression. Whether you're a content creator or a fan, our platform is designed to bring out the best in creativity, connection, and community. Share intimate moments, unlock exclusive content, and discover a new way to connect with your favorite creators like never before.</p></div>
    <div class="sec-title" style="left:19px;top:183px">Explore</div>
    <div class="card" style="left:19px;top:217px"><div class="thumb" role="img" aria-label="Video thumbnail of a creator"><span class="dur">30:00</span></div><div class="title">Video Title</div><div class="creator">Creator</div></div>
    <div class="card" style="left:209px;top:217px"><div class="thumb hi" role="img" aria-label="Video thumbnail of a creator"><span class="dur">30:00</span></div><div class="title">Video Title</div><div class="creator">Creator</div></div>
    <div class="card" style="left:399px;top:217px"><div class="thumb" role="img" aria-label="Video thumbnail of a creator"><span class="dur">30:00</span></div><div class="title">Video Title</div><div class="creator">Creator</div></div>
    <svg class="pointer" style="left:362px;top:325px" width="22" height="22"><use href="#arrow"/></svg>
  </section>

  <!-- Dashboard, logged in (two states) -->
  <section class="screen" style="left:604px;top:786px">
    <header class="topbar">
      <div class="brand sm">Velmora</div>
      <div class="mode-toggle" style="left:476px;top:10px"><svg class="eye" width="12" height="10"><use href="#eye"/></svg><div class="knob"><svg width="14" height="10"><use href="#oval"/></svg></div></div>
      <div class="avatar-btn" style="left:544px;top:10px"><svg width="14" height="16"><use href="#person"/></svg></div>
    </header>
    <div class="tile" style="left:18px;top:72px"><svg width="32" height="32"><circle cx="16" cy="16" r="15" fill="#111"/></svg><span>Start Live</span></div>
    <div class="tile" style="left:116px;top:72px"><svg width="32" height="32"><rect x="1" y="6" width="30" height="21" fill="#111"/><path d="M1 6L16 18L31 6" fill="none" stroke="#fff" stroke-width="1.6"/></svg><span>Inbox</span></div>
    <div class="tile" style="left:213px;top:72px"><svg width="32" height="32" style="color:#666"><use href="#gift"/></svg><span>Manage Subs</span></div>
    <div class="tile" style="left:311px;top:72px"><svg width="32" height="32"><circle cx="16" cy="16" r="10" fill="none" stroke="#111" stroke-width="1.8"/></svg><span>Manage Channel</span></div>
    <div class="tile" style="left:408px;top:72px"><svg width="32" height="32"><path d="M5 20V15C5 4 27 4 27 15V20" fill="none" stroke="#111" stroke-width="2.5"/><rect x="3" y="17" width="6" height="11" rx="2" fill="#111"/><rect x="23" y="17" width="6" height="11" rx="2" fill="#111"/></svg><span>Contact Support</span></div>
    <div class="sec-title" style="left:19px;top:183px">Explore <small>See more</small></div>
    <div class="card" style="left:18px;top:217px"><div class="thumb" role="img" aria-label="Video thumbnail of a creator"><span class="dur">30:00</span></div><div class="title">Video Title</div><div class="creator">Creator</div></div>
    <div class="card" style="left:209px;top:217px"><div class="thumb hi" role="img" aria-label="Video thumbnail of a creator"><span class="dur">30:00</span></div><div class="title">Video Title</div><div class="creator">Creator</div></div>
    <div class="card" style="left:399px;top:217px"><div class="thumb" role="img" aria-label="Video thumbnail of a creator"><span class="dur">30:00</span></div><div class="title">Video Title</div><div class="creator">Creator</div></div>
    <svg class="pointer" style="left:362px;top:325px" width="22" height="22"><use href="#arrow"/></svg>
  </section>

  <section class="screen" style="left:604px;top:1172px">
    <header class="topbar">
      <div class="brand sm">Velmora</div>
      <div class="mode-toggle" style="left:476px;top:10px"><svg class="eye" width="12" height="10"><use href="#eye"/></svg><div class="knob"><svg width="14" height="10"><use href="#oval"/></svg></div></div>
      <div class="avatar-btn" style="left:544px;top:10px"><svg width="14" height="16"><use href="#person"/></svg></div>
    </header>
    <div class="tile" style="left:18px;top:72px"><svg width="32" height="32"><circle cx="16" cy="16" r="15" fill="#111"/></svg><span>Start Live</span></div>
    <div class="tile" style="left:116px;top:72px"><svg width="32" height="32"><rect x="1" y="6" width="30" height="21" fill="#111"/><path d="M1 6L16 18L31 6" fill="none" stroke="#fff" stroke-width="1.6"/></svg><span>Inbox</span></div>
    <div class="tile" style="left:213px;top:72px"><svg width="32" height="32" style="color:#666"><use href="#gift"/></svg><span>Manage Subs</span></div>
    <div class="tile" style="left:311px;top:72px"><svg width="32" height="32"><circle cx="16" cy="16" r="10" fill="none" stroke="#111" stroke-width="1.8"/></svg><span>Manage Channel</span></div>
    <div class="tile" style="left:408px;top:72px"><svg width="32" height="32"><path d="M5 20V15C5 4 27 4 27 15V20" fill="none" stroke="#111" stroke-width="2.5"/><rect x="3" y="17" width="6" height="11" rx="2" fill="#111"/><rect x="23" y="17" width="6" height="11" rx="2" fill="#111"/></svg><span>Contact Support</span></div>
    <div class="sec-title" style="left:19px;top:183px">Explore <small>See more</small></div>
    <div class="card" style="left:18px;top:217px"><div class="thumb" role="img" aria-label="Video thumbnail of a creator"><span class="dur">30:00</span></div><div class="title">Video Title</div><div class="creator">Creator</div></div>
    <div class="card" style="left:209px;top:217px"><div class="thumb hi" role="img" aria-label="Video thumbnail of a creator"><span class="dur">30:00</span></div><div class="title">Video Title</div><div class="creator">Creator</div></div>
    <div class="card" style="left:399px;top:217px"><div class="thumb" role="img" aria-label="Video thumbnail of a creator"><span class="dur">30:00</span></div><div class="title">Video Title</div><div class="creator">Creator</div></div>
    <svg class="pointer" style="left:362px;top:325px" width="22" height="22"><use href="#arrow"/></svg>
  </section>

</main>
</body>
</html>
```